Dental Hygiene referral cards

I am looking to make some referral cards for our hygienists for our dental office. something with our logo and address on the front, and on the back have
hygienist:
__________________
Referred by:
__________________
with a little blurb about what we will give away for a referral.

attached to this is our logo, and a drawing of what im looking for.

I will need this for two of our offices, so just the logo and address will change.

```html
<!DOCTYPE html>
<html lang="en">
<head>
<meta charset="utf-8">
<title>Harbor Ridge Dental – Referral Card</title>
<link href="https://fonts.googleapis.com/css2?family=Cinzel:wght@500&family=Open+Sans:wght@400;600;700&display=swap" rel="stylesheet">
<style>
  :root {
    --navy: #003f7d;
    --slate: #9a9a9b;
    --ink-grey: #8c8d8f;
    --white: #ffffff;
    --bg-top: #e6e7e9;
    --bg-bottom: #b3b4b7;
  }
  * { margin: 0; padding: 0; box-sizing: border-box; }
  html, body { width: 1190px; height: 1200px; overflow: hidden; }
  body {
    position: relative;
    background: linear-gradient(180deg, var(--bg-top), var(--bg-bottom));
    font-family: "Open Sans", Arial, sans-serif;
  }
  .card {
    position: absolute;
    left: 173px;
    width: 844px;
    height: 483px;
    background: var(--white);
    overflow: hidden;
    box-shadow: 0 3px 8px rgba(0,0,0,0.22);
  }
  .card-front { top: 106px; border-radius: 23px; }
  .card-back { top: 633px; height: 482px; border-radius: 46px; }

  .brand-name {
    font-family: "Cinzel", Georgia, serif;
    font-weight: 500;
    color: var(--navy);
    text-align: center;
    line-height: 1;
  }
  .card-front .brand-name {
    position: absolute; left: 0; right: 0; top: 40px;
    font-size: 50px;
  }
  .card-front .brand-name span { display: block; margin-top: 8px; font-size: 40px; letter-spacing: 10px; }

  .person {
    position: absolute; left: 0; right: 0; top: 180px;
    text-align: center;
    font-family: "Cinzel", Georgia, serif;
  }
  .person-name { font-size: 34px; color: var(--navy); font-weight: 500; line-height: 1.1; }
  .person-role { font-size: 25px; color: var(--ink-grey); line-height: 1.2; }

  .contact-band {
    position: absolute; left: 0; right: 0; top: 282px; height: 156px;
    background: var(--navy);
    color: var(--white);
    font-size: 17px;
  }
  .contact-list { position: absolute; left: 28px; top: 30px; list-style: none; }
  .contact-list li { display: flex; align-items: center; height: 36px; }
  .contact-list svg { width: 17px; height: 17px; margin-right: 10px; fill: none; stroke: var(--white); stroke-width: 1.8; }
  .contact-list .phone-icon { fill: var(--white); stroke: none; }
  .address {
    position: absolute; right: 25px; top: 49px;
    text-align: right; font-size: 19px; line-height: 30px;
  }

  .back-brand {
    position: absolute; left: 0; width: 416px; top: 240px;
  }
  .back-brand .brand-name { font-size: 38px; }
  .back-brand .brand-name span { display: block; margin-top: 6px; font-size: 30px; letter-spacing: 8px; }

  .referral-panel {
    position: absolute; left: 416px; top: 0; right: 0; bottom: 0;
    color: var(--white);
  }
  .offer { height: 171px; background: var(--slate); padding: 12px 0 0 28px; font-size: 34px; font-weight: 600; line-height: 49px; }
  .field { padding-left: 32px; font-size: 23px; font-weight: 700; display: flex; align-items: center; }
  .field-hygienist { height: 82px; background: var(--navy); }
  .field-referrer { height: 59px; background: var(--slate); }
  .blurb { height: 170px; background: var(--navy); padding: 16px 0 0 32px; font-size: 19.5px; line-height: 36.5px; }
</style>
</head>
<body>

<section class="card card-front">
  <h1 class="brand-name">Harbor Ridge<span>Dental</span></h1>
  <div class="person">
    <p class="person-name">Nora Whitfield</p>
    <p class="person-role">Doctor</p>
  </div>
  <div class="contact-band">
    <ul class="contact-list">
      <li><svg class="phone-icon" viewBox="0 0 24 24"><path d="M6.6 10.8a15.1 15.1 0 0 0 6.6 6.6l2.2-2.2a1 1 0 0 1 1-.25 11.4 11.4 0 0 0 3.6.57 1 1 0 0 1 1 1V20a1 1 0 0 1-1 1A17 17 0 0 1 3 4a1 1 0 0 1 1-1h3.5a1 1 0 0 1 1 1c0 1.25.2 2.45.57 3.6a1 1 0 0 1-.25 1z"/></svg>012-555-0147</li>
      <li><svg viewBox="0 0 24 24"><rect x="2.5" y="5" width="19" height="14"/><path d="M2.5 5l9.5 8 9.5-8M2.5 19l7-7M21.5 19l-7-7"/></svg>office@harborridgedental.com</li>
      <li><svg viewBox="0 0 24 24"><circle cx="12" cy="12" r="9.5"/><ellipse cx="12" cy="12" rx="4.2" ry="9.5"/><path d="M2.5 12h19M4 7h16M4 17h16"/></svg>www.harborridgedental.com</li>
    </ul>
    <p class="address">123, Street Name, City Name<br>Zipcode - 01234</p>
  </div>
</section>

<section class="card card-back">
  <div class="back-brand">
    <p class="brand-name">Harbor Ridge<span>Dental</span></p>
  </div>
  <div class="referral-panel">
    <p class="offer">Free<br>Brightwave<br>Toothbrush</p>
    <p class="field field-hygienist">Hygienist:</p>
    <p class="field field-referrer">Referred by:</p>
    <p class="blurb">Refer A Patient For An Exam and<br>A Cleaning and Both of You Will Receive<br>A Free Brightwave Toothbrush!</p>
  </div>
</section>

</body>
</html>
```